Modern card design needed for building development company

We are looking for a sharp modern new look for our business cards.
We are a New Zealand based company called TKV Ventures NZ LTD that specialises in subdividing large sections, housing and commercial buildings.
We have attached a photo of the current logo and would like to see it improved somehow as it looks a bit dated.
We are open to any colours.

Target Market(s)

Investors, Property buyers

Industry/Entity Type

Investment

Contact Information for Business Card

TKV VENTURES NZ LTD
www.tkvventuresnz.co.nz

Howard Pennick
Phone +64 21 843 192
Email hdpennick@fernmail.co.nz

Font styles to use
Serif
Sans Serif

Colors
0792cd
33a6d7
85cae6
6b449b
886aae
f04a50
ec1f27
f37122
f68d4d

Requirements
Must have
• Please try and make the logo more modern or if you have a similar one we would like to see it.

```html
<!DOCTYPE html>
<html lang="en">
<head>
<meta charset="utf-8">
<title>TKV Ventures NZ – Business Card</title>
<link href="https://fonts.googleapis.com/css2?family=Open+Sans:wght@400;700&display=swap" rel="stylesheet">
<style>
  :root {
    --backdrop: #5b3b27;
    --card: #ffffff;
    --brand-blue: #1f5591;
    --text-grey: #3c3f44;
    --icon-grey: #4a4d52;
  }
  * { margin: 0; padding: 0; box-sizing: border-box; }
  html, body { width: 1200px; height: 1000px; overflow: hidden; }
  body {
    background: var(--backdrop);
    font-family: "Open Sans", Arial, sans-serif;
    position: relative;
  }
  .card {
    position: absolute;
    left: 266px;
    width: 666px;
    height: 397px;
    background: var(--card);
    box-shadow: 0 6px 14px rgba(0,0,0,0.35);
  }
  .card--front { top: 74px; }
  .card--back { top: 534px; }

  .brand {
    position: absolute;
    display: flex;
    flex-direction: column;
    align-items: center;
    color: var(--brand-blue);
    font-weight: 700;
    text-align: center;
    line-height: 1;
  }
  .brand__square { background: var(--brand-blue); }
  .card--front .brand { left: 0; width: 666px; top: 100px; }
  .card--front .brand__square { width: 90px; height: 90px; margin-bottom: 40px; }
  .card--front .brand__name { font-size: 40px; }
  .card--front .brand__sub { font-size: 30px; margin-top: 6px; }

  .card--back .brand { left: 30px; width: 320px; top: 120px; }
  .card--back .brand__square { width: 74px; height: 74px; margin-bottom: 36px; }
  .card--back .brand__name { font-size: 33px; }
  .card--back .brand__sub { font-size: 25px; margin-top: 5px; }

  .contact {
    position: absolute;
    left: 374px;
    top: 114px;
    color: var(--text-grey);
    font-size: 15px;
  }
  .contact__name {
    color: var(--brand-blue);
    font-weight: 700;
    font-size: 19px;
    text-transform: uppercase;
    line-height: 1.2;
  }
  .contact__role { line-height: 1.4; }
  .contact__company { margin-top: 18px; margin-bottom: 14px; }
  .contact__list { list-style: none; }
  .contact__item { display: flex; align-items: center; height: 22px; }
  .contact__icon { width: 14px; height: 14px; margin-right: 7px; fill: var(--icon-grey); }
</style>
</head>
<body>
  <section class="card card--front">
    <div class="brand">
      <span class="brand__square"></span>
      <span class="brand__name">TKV VENTURES</span>
      <span class="brand__sub">NZ</span>
    </div>
  </section>

  <section class="card card--back">
    <div class="brand">
      <span class="brand__square"></span>
      <span class="brand__name">TKV VENTURES</span>
      <span class="brand__sub">NZ</span>
    </div>
    <div class="contact">
      <p class="contact__name">Howard Pennick</p>
      <p class="contact__role">Founder / CEO</p>
      <p class="contact__company">TKV Ventures NZ LTD</p>
      <ul class="contact__list">
        <li class="contact__item">
          <svg class="contact__icon" viewBox="0 0 16 16"><path d="M2 5c0-2 2-3 6-3s6 1 6 3v1h-3V5H5v1H2z M4 7h8l2 6H2z"/></svg>
          +64 21 843 192
        </li>
        <li class="contact__item">
          <svg class="contact__icon" viewBox="0 0 16 16"><path d="M1 3h14v10H1z" fill="none" stroke="#4a4d52" stroke-width="1.6"/><path d="M1 3l7 6 7-6" fill="none" stroke="#4a4d52" stroke-width="1.6"/></svg>
          hdpennick@fernmail.co.nz
        </li>
        <li class="contact__item">
          <svg class="contact__icon" viewBox="0 0 16 16"><circle cx="8" cy="8" r="6.5" fill="none" stroke="#4a4d52" stroke-width="1.6"/><path d="M1.5 8h13M8 1.5c-3 3-3 10 0 13M8 1.5c3 3 3 10 0 13" fill="none" stroke="#4a4d52" stroke-width="1.2"/></svg>
          www.tkvventuresnz.co.nz
        </li>
      </ul>
    </div>
  </section>
</body>
</html>
```